Real Estate Renovation and Rental:Business Card/Logo Design Project

Corliss Grove LLC is a small partnership that buys homes to renovate, then provide as rentals to people who may not currently be able to purchase a home - but we also coach them on how to improve their credit so that, in 2-5 years, they may be able to buy a home. Maybe even the one they're living in.

We are based in Sonoma County of Northern California, operating in communities including Healdsburg, Windsor, Santa Rosa, and Cloverdale.

Please design a business card, but the same logo should work for signs that we will post on the homes as they are being renovated.

The design should be clean, contemporary, professional but warm. I'd love to see a rooftop feature, or some other element of a house. Again, not too much detail, clean and welcoming. The design must include "Corliss Grove LLC" - but "CGLLC" could also be used as a primary name, with "Corliss Grove LLC" in smaller print somewhere. If using "CGLLC", the CG could be visually distinct (larger, different color, font) than the LLC part of the name but they must be together.
Updates

just conferring with partner to choose a final design ... should be ready to choose soon and will post

Industry/Entity Type

Business

Requirements
Must have
• the name "Corliss Grove LLC"
for business card design, and leave room for us to customize with partner names, address, telephone numbers, email addresses
Nice to have
• some element of a house included

```html
<!DOCTYPE html>
<html lang="en">
<head>
<meta charset="utf-8">
<title>Corliss Grove LLC – Business Card</title>
<link href="https://fonts.googleapis.com/css2?family=Roboto:wght@300;400;700&display=swap" rel="stylesheet">
<style>
  :root {
    --page-bg: #e9e9e9;
    --card-green: #4b7555;
    --card-green-dark: #436c4d;
    --logo-cream: #e8ede2;
    --text-sage: #a8c1ab;
    --text-sage-soft: #8fae95;
    --divider: #9fb9a3;
  }
  * { margin: 0; padding: 0; box-sizing: border-box; }
  html, body {
    width: 1200px;
    height: 1000px;
    overflow: hidden;
    background: var(--page-bg);
    font-family: "Roboto", Arial, sans-serif;
  }
  .stage {
    width: 1200px;
    height: 1000px;
    display: flex;
    align-items: center;
    justify-content: center;
  }
  .business-card {
    position: relative;
    width: 1000px;
    height: 572px;
    background: radial-gradient(ellipse at 60% 45%, var(--card-green) 0%, var(--card-green-dark) 100%);
    box-shadow: 0 8px 24px rgba(0,0,0,0.18);
    color: var(--text-sage);
  }
  .brand {
    position: absolute;
    left: 70px;
    top: 70px;
    display: flex;
    align-items: center;
    gap: 22px;
  }
  .brand-square {
    width: 34px;
    height: 34px;
    background: var(--logo-cream);
  }
  .brand-name {
    font-weight: 300;
    font-size: 62px;
    letter-spacing: 1px;
    color: var(--logo-cream);
  }
  .person {
    position: absolute;
    left: 230px;
    top: 220px;
    display: flex;
    align-items: baseline;
    gap: 16px;
  }
  .person-name {
    font-weight: 700;
    font-size: 40px;
    color: var(--text-sage);
  }
  .person-divider {
    width: 2px;
    height: 38px;
    background: var(--divider);
    align-self: center;
  }
  .person-role {
    font-weight: 300;
    font-size: 26px;
    color: var(--text-sage);
  }
  .contact {
    position: absolute;
    left: 230px;
    top: 310px;
    font-size: 25px;
    line-height: 40px;
    font-weight: 300;
  }
  .contact-line { white-space: nowrap; }
  .contact-line.indent-1 { padding-left: 70px; }
  .contact-line.indent-2 { padding-left: 110px; }
  .contact-label { font-weight: 700; }
  .contact-gap { display: inline-block; width: 18px; }
  .address {
    position: absolute;
    left: 70px;
    right: 70px;
    bottom: 46px;
    text-align: center;
    font-size: 24px;
    font-weight: 300;
    color: var(--text-sage-soft);
  }
</style>
</head>
<body>
  <main class="stage">
    <article class="business-card">
      <header class="brand">
        <span class="brand-square"></span>
        <span class="brand-name">Corliss Grove LLC</span>
      </header>

      <div class="person">
        <span class="person-name">Daniel Reyes</span>
        <span class="person-divider"></span>
        <span class="person-role">Sales Director</span>
      </div>

      <div class="contact">
        <p class="contact-line"><span class="contact-label">Office:</span> +1 707 555 0142<span class="contact-gap"></span><span class="contact-label">Mobile:</span> +1 707 555 0187</p>
        <p class="contact-line indent-1"><span class="contact-label">Email:</span> danielr@corlissgrovellc.com</p>
        <p class="contact-line indent-2"><span class="contact-label">Web:</span> www.corlissgrovellc.com</p>
      </div>

      <p class="address">Address line, Lorem ipsum dolor sit amet, Consectetur adipisicing elit</p>
    </article>
  </main>
</body>
</html>
```